Amber Meadow LLC business card

I help with the Marketing and Sales of various Natural, Organic, Eco Friendly and Healthy Main Stream products to Retail Corporate accounts as well as Independents and Distributors.I also highlight Private label items to these same Retail Corporate accounts.Cherish the Moments, Enjoy Life!

Speciality & Health Sales and Marketing

Target Market(s)

Men and Women

Industry/Entity Type

Business

Contact Information for Business Card

Amber Meadow, LLC
Lydia Rose Vandermeer
427 West Orchard Lane
Ste 5-384
Phoenix, AZ 85317
602-718-3054
lvandermeer@pinemail.net

Requirements
Must have
• Nice, femine font
Something in the background or on a side with a softness
Nice to have
• Cherish the Moments, Enjoy Life
Should not have
• Hardness

```html
<!DOCTYPE html>
<html lang="en">
<head>
<meta charset="utf-8">
<title>Amber Meadow, LLC – Business Card</title>
<link rel="stylesheet" href="https://fonts.googleapis.com/css2?family=Damion&family=Caveat:wght@500&family=Libre+Baskerville:ital,wght@0,700;1,400&family=Hind:wght@300&display=swap">
<style>
  :root {
    --paper: #ffffff;
    --ink: #2b2b2b;
    --rose: #e0194f;
    --rose-soft: #f0a3b8;
    --frame: #333333;
  }
  html, body {
    margin: 0;
    width: 1200px;
    height: 850px;
    overflow: hidden;
    background: var(--paper);
  }
  .canvas {
    position: relative;
    width: 1200px;
    height: 850px;
  }
  .card {
    position: absolute;
    left: 57px;
    top: 105px;
    width: 1084px;
    height: 636px;
    border: 2px solid var(--frame);
  }
  .company {
    position: absolute;
    left: 190px;
    top: 203px;
    width: 315px;
    margin: 0;
    text-align: center;
    font-family: "Damion", cursive;
    font-weight: 400;
    font-size: 56px;
    line-height: 78px;
    color: var(--rose);
  }
  .person {
    position: absolute;
    left: 130px;
    top: 548px;
    width: 435px;
    margin: 0;
    text-align: center;
    font-family: "Libre Baskerville", serif;
    font-weight: 700;
    font-size: 30px;
    color: var(--ink);
  }
  .services {
    position: absolute;
    left: 660px;
    top: 188px;
    width: 430px;
    margin: 0;
    text-align: center;
    font-family: "Libre Baskerville", serif;
    font-style: italic;
    font-weight: 400;
    font-size: 35px;
    line-height: 52px;
    color: var(--ink);
  }
  .flower-mark {
    position: absolute;
    left: 830px;
    top: 325px;
    width: 90px;
    height: 125px;
    border-radius: 45px 45px 20px 20px;
    background: linear-gradient(180deg, var(--rose) 0%, var(--rose-soft) 100%);
  }
  .contact {
    position: absolute;
    left: 674px;
    top: 478px;
    width: 402px;
    margin: 0;
    font-family: "Hind", sans-serif;
    font-weight: 300;
    font-style: normal;
    font-size: 32px;
    line-height: 42px;
    color: var(--ink);
  }
  .contact-line {
    display: block;
    text-align: justify;
    text-align-last: justify;
    letter-spacing: 0.5px;
  }
  .contact-line.phone { letter-spacing: 10px; }
  .motto {
    position: absolute;
    left: 660px;
    top: 668px;
    width: 430px;
    margin: 0;
    text-align: center;
    font-family: "Caveat", cursive;
    font-weight: 500;
    font-size: 34px;
    color: var(--rose);
  }
</style>
</head>
<body>
<main class="canvas">
  <section class="card">
  </section>
  <h1 class="company">Amber<br>Meadow,<br>LLC</h1>
  <p class="person">Lydia Rose Vandermeer</p>
  <p class="services">Speciality &amp; Health<br>Sales and Marketing</p>
  <div class="flower-mark" role="img" aria-label="Small single flower illustration in rose pink"></div>
  <address class="contact">
    <span class="contact-line">427 West Orchard Lane Ste</span>
    <span class="contact-line">5-384 Phoenix, AZ 85317</span>
    <span class="contact-line phone">602-718-3054</span>
    <span class="contact-line">lvandermeer@pinemail.net</span>
  </address>
  <p class="motto">Cherish the Moments, Enjoy Life!</p>
</main>
</body>
</html>
```